Vice chair

I'm running for a position as vice chair this will be posted in the lunch room cafeteria in this package i posted logos, my picture, sample of old flyers to give you a idea i also wrote literature need help in putting it together like it to look like a million bucks goal win this election I summited lots of pdf files and jpeg look though them to help with your design feel free to contact me to further assist you
Updates

Would like this to be completed by Wednesday

Target Market(s)

My constituents

Font styles to use
Serif

Colors

Designer to choose colors to be used in the design.

Requirements
Must have
• Make it look clean neat
Nice to have
• Nice background

```html
<!DOCTYPE html>
<html lang="en">
<head>
<meta charset="utf-8">
<title>Ray Delgado – Vice Chair</title>
<link href="https://fonts.googleapis.com/css2?family=Oswald:wght@400;600;700&family=Lato:ital,wght@0,400;0,700;0,900;1,400;1,700&display=swap" rel="stylesheet">
<style>
:root{
  --bg:#3a3a3c;
  --red:#e5283a;
  --red-deep:#b8172a;
  --pink:#f04a5a;
  --ink:#141416;
  --charcoal:#2b2b2e;
  --white:#ffffff;
  --paper:#f1f1f2;
  --navy:#20264d;
  --gold:#f2b51c;
  --text:#3c3c40;
}
*{margin:0;padding:0;box-sizing:border-box}
html,body{width:1200px;height:960px;overflow:hidden}
body{background:var(--bg);font-family:"Lato",sans-serif}
.flyer{position:absolute;left:280px;top:28px;width:640px;height:904px;overflow:hidden;background:var(--paper);box-shadow:0 18px 40px rgba(0,0,0,.45)}
.flyer-art{position:absolute;inset:0}
.abs{position:absolute}
.name-first{left:372px;top:70px;font:600 34px/1 "Oswald",sans-serif;color:var(--white);letter-spacing:2px}
.name-last{left:340px;top:110px;background:var(--red);color:var(--white);padding:6px 18px;font:700 62px/1 "Oswald",sans-serif;letter-spacing:3px;box-shadow:0 4px 10px rgba(0,0,0,.35)}
.tagline{left:380px;top:196px;background:var(--white);color:var(--red);padding:4px 14px;font:600 28px/1 "Oswald",sans-serif;letter-spacing:1px}
.tagline small{font:italic 700 16px "Lato",sans-serif;color:var(--red-deep);margin:0 4px}
.values{left:30px;top:330px;width:330px;color:var(--white)}
.values-kicker{font:400 18px/1 "Oswald",sans-serif}
.values-title{font:700 28px/1 "Oswald",sans-serif;letter-spacing:1px}
.values-sub{font:400 8px/1.3 "Lato",sans-serif;opacity:.85;margin:4px 0 10px}
.values-sub b{font-weight:900}
.values-body{font:400 15px/1.3 "Lato",sans-serif}
.values-note{font:400 9px/1.3 "Lato",sans-serif;margin-top:8px;opacity:.9}
.slate{left:392px;top:474px;width:230px;white-space:nowrap;font:700 40px/1 "Oswald",sans-serif;color:var(--red);letter-spacing:1px}
.slate em{font:italic 700 20px "Lato",sans-serif;color:var(--white);margin:0 5px}
.ballot{left:520px;top:540px;width:62px;height:62px;background:var(--red);border:4px solid var(--white);color:var(--white);font:700 44px/52px "Oswald",sans-serif;text-align:center}
.tenure{left:394px;top:530px;width:84px;height:84px;border-radius:50%;background:var(--white);text-align:center;padding-top:13px}
.tenure-num{font:700 30px/1 "Oswald",sans-serif;color:var(--red)}
.tenure-unit{font:700 13px/1 "Oswald",sans-serif;color:var(--red)}
.tenure-note{font:400 8px/1.2 "Lato",sans-serif;color:var(--navy)}
.mission-badge{left:40px;top:640px;width:150px;height:150px;border-radius:50%;background:radial-gradient(circle at 40% 40%,#f7c63d,var(--gold))}
.intro{left:230px;top:650px;width:380px;font:400 10px/1.4 "Lato",sans-serif;color:var(--text)}
.intro p{margin-bottom:8px}
.intro .who{color:var(--red);font-weight:700}
.intro .ask{color:var(--red);font-weight:700;font-style:italic}
.closing{left:0;top:800px;width:640px;background:var(--ink);padding:10px 30px;text-align:center}
.closing-lead{font:600 12px/1.3 "Oswald",sans-serif;color:var(--red);text-transform:uppercase;letter-spacing:.5px}
.closing-body{font:italic 400 11px/1.4 "Lato",sans-serif;color:var(--white)}
.footer{left:0;top:858px;width:640px;height:46px;background:var(--red);color:var(--white);display:flex;align-items:center;justify-content:center;gap:12px;font:400 22px/1 "Oswald",sans-serif}
.footer b{font-weight:700}
.footer .role{font-weight:700;font-size:28px;margin-left:20px}
</style>
</head>
<body>
<main class="flyer">
  <svg class="flyer-art" width="640" height="904" viewBox="0 0 640 904">
    <defs>
      <radialGradient id="flag-field" cx="0.1" cy="0.05" r="0.7">
        <stop offset="0" stop-color="#2a3163"/>
        <stop offset=".55" stop-color="#3a3466" stop-opacity=".8"/>
        <stop offset="1" stop-color="#3a3466" stop-opacity="0"/>
      </radialGradient>
      <linearGradient id="flag" x1="0" y1="0" x2="1" y2="1">
        <stop offset="0" stop-color="#5a3356"/>
        <stop offset=".4" stop-color="#c8283a"/>
        <stop offset=".7" stop-color="#e2504a"/>
        <stop offset="1" stop-color="#f0803c"/>
      </linearGradient>
      <linearGradient id="portrait" x1="0" y1="0" x2="0" y2="1">
        <stop offset="0" stop-color="#8a5a42"/>
        <stop offset="1" stop-color="#1c1a1a"/>
      </linearGradient>
      <linearGradient id="sheet" x1="0" y1="0" x2="1" y2="0">
        <stop offset="0" stop-color="#ffffff"/>
        <stop offset="1" stop-color="#d9d9dc"/>
      </linearGradient>
    </defs>
    <g role="img" aria-label="Waving American flag background with stars and stripes">
      <rect width="640" height="460" fill="url(#flag)"/>
      <rect width="640" height="460" fill="url(#flag-field)"/>
    </g>
    <rect x="30" y="20" width="290" height="300" fill="url(#portrait)" role="img" aria-label="Portrait photo of the candidate"/>
    <rect x="0" y="460" width="640" height="200" fill="var(--charcoal)"/>
    <polygon points="0,300 380,300 300,620 0,620" fill="var(--red)"/>
    <polygon points="0,620 640,620 640,800 0,800" fill="url(#sheet)"/>
    <polygon points="0,560 300,620 0,620" fill="var(--pink)" opacity=".6"/>
    <circle cx="430" cy="290" r="46" fill="#e87a1e" stroke="#ffffff" stroke-width="4"/>
    <circle cx="530" cy="300" r="48" fill="#1d3a8a" stroke="#ffffff" stroke-width="4"/>
    <circle cx="580" cy="400" r="46" fill="#e0c230" stroke="#b8172a" stroke-width="4"/>
  </svg>

  <div class="abs name-first">RAY</div>
  <div class="abs name-last">DELGADO</div>
  <div class="abs tagline">TIME <small>for</small> CHANGE</div>

  <section class="abs values">
    <div class="values-kicker">Respect &amp;</div>
    <div class="values-title">INTEGRITY</div>
    <div class="values-sub">Transit Workers Guild will be the <b>BACKBONE</b> that shapes our union</div>
    <p class="values-body">Past union member of Haulers local 412 believes in There is a collective bargaining agreement in place and no management is above the law to violate it.</p>
    <p class="values-note">Past union member of Haulers local 738 believes a house that is divided cannot stand alone</p>
  </section>

  <div class="abs slate">VOTE<em>the</em>SLATE</div>
  <div class="abs tenure">
    <div class="tenure-num">20</div>
    <div class="tenure-unit">YEARS</div>
    <div class="tenure-note">ON THE JOB</div>
  </div>
  <div class="abs ballot">X</div>

  <div class="abs mission-badge" role="img" aria-label="Vote with your mission badge with check mark"></div>

  <section class="abs intro">
    <p><span class="who">I Ray Delgado</span> for those who don't know me would like to introduce myself I have always been approachable and helpful whether you are a probationary officer or a veteran operator with knowledge or information, we must protect our union rules for ourselves our future and most important our children.</p>
    <p>I would like this opportunity to run as your vice chair a person you can trust and believe in me positive and motivations are my main keys for progress and for change in my campaign when there is no leader to look up to one therefore must become one I do believe I'm the right person for this position so</p>
    <p class="ask">Please come out and support me and vote me as your vice chair.</p>
  </section>

  <section class="abs closing">
    <p class="closing-lead">In closing I believe that our union does not stand out individually achievement for all</p>
    <p class="closing-body">we must always continue to stand together, stay together &amp; fight together so we can win together because success is never owned, it is rented and the rent is due every day.</p>
  </section>

  <footer class="abs footer"><b>VOTE</b> independent me as your <span class="role">VICE CHAIR</span></footer>
</main>
</body>
</html>
```